Bright, Fun and hard to forget home inspection business card.

We need a Business card design for a new Home Inspection company. We are building a brand that is bright, fun and easy to remember.

Target Market(s)

Anyone involed in buying and selling of homes.

Industry/Entity Type

Home Inspection

Contact Information for Business Card

Colin Marlowe Owner/Inspector

Wedsite- PorchAndRafterCheck.example
Phone: 253-555-0187
Email- ColinMarlowe@mailbox.example
WA Lic # 4806

Requirements
Must have
• BRQV LOGO somewhere on card.

```html
<!DOCTYPE html>
<html lang="en">
<head>
<meta charset="utf-8">
<title>Porch and Rafter Check — Business Card</title>
<link href="https://fonts.googleapis.com/css2?family=Lato:wght@400;700;900&display=swap" rel="stylesheet">
<style>
  :root {
    --bg: #d9d9d9;
    --card-white: #ffffff;
    --brand-orange: #f05a28;
    --ink: #1c1c1c;
    --ink-soft: #2e2e2e;
    --night: #050505;
    --badge-red: #d8313f;
  }
  * { margin: 0; padding: 0; box-sizing: border-box; }
  html, body { width: 1200px; height: 926px; overflow: hidden; }
  body {
    background: var(--bg);
    font-family: "Lato", Arial, sans-serif;
    position: relative;
  }
  .card {
    position: absolute;
    left: 240px;
    width: 720px;
    height: 411px;
    overflow: hidden;
    box-shadow: 0 6px 18px rgba(0,0,0,0.18);
  }
  .card--front { top: 34px; background: var(--card-white); }
  .card--back { top: 481px; background: var(--night); }

  .card__wave { position: absolute; inset: 0; }

  .brand {
    display: flex;
    align-items: center;
    gap: 12px;
    font-weight: 900;
    text-transform: uppercase;
    line-height: 1;
    white-space: nowrap;
  }
  .brand__dot {
    border-radius: 50%;
    background: var(--brand-orange);
    flex: none;
  }
  .card--front .brand {
    position: absolute;
    left: 34px; top: 38px;
    color: var(--ink);
    font-size: 27px;
  }
  .card--front .brand__dot { width: 34px; height: 34px; }

  .back-center {
    position: absolute;
    inset: 0;
    display: flex;
    align-items: center;
    justify-content: center;
  }
  .card--back .brand {
    color: var(--card-white);
    font-size: 34px;
    gap: 16px;
  }
  .card--back .brand__dot { width: 44px; height: 44px; }

  .person { position: absolute; left: 438px; top: 128px; text-align: center; width: 240px; }
  .person__name { font-weight: 900; font-size: 27px; color: var(--ink); }
  .person__role { font-weight: 400; font-size: 16px; color: var(--ink-soft); margin-top: 2px; }

  .contact {
    position: absolute;
    left: 30px;
    top: 268px;
    list-style: none;
    color: var(--card-white);
    font-size: 17px;
  }
  .contact__item { display: flex; align-items: center; gap: 8px; margin-bottom: 7px; }
  .contact__icon {
    width: 20px; height: 20px;
    background: var(--card-white);
    border-radius: 4px;
    flex: none;
  }

  .cert-badge {
    position: absolute;
    left: 456px;
    top: 226px;
    width: 112px;
    height: 112px;
  }
  .license {
    position: absolute;
    left: 456px;
    top: 360px;
    color: var(--card-white);
    font-size: 18px;
    font-weight: 700;
  }
</style>
</head>
<body>

<section class="card card--front" aria-label="Business card front">
  <svg class="card__wave" viewBox="0 0 720 411" preserveAspectRatio="none" aria-hidden="true">
    <path d="M0,212 C150,168 290,250 450,236 C560,226 640,238 720,250 L720,411 L0,411 Z" fill="var(--brand-orange)"/>
  </svg>

  <div class="brand">
    <span class="brand__dot"></span>
    <span>Porch and Rafter Check LLC</span>
  </div>

  <div class="person">
    <p class="person__name">Colin Marlowe</p>
    <p class="person__role">Owner/Inspector</p>
  </div>

  <ul class="contact">
    <li class="contact__item">
      <svg class="contact__icon" viewBox="0 0 20 20" aria-hidden="true">
        <path d="M6 4 L8.5 4 L9.5 7 L8 8.3 C8.8 10 10 11.2 11.7 12 L13 10.5 L16 11.5 L16 14 C16 15 15 16 14 16 C8.5 15.5 4.5 11.5 4 6 C4 5 5 4 6 4 Z" fill="var(--ink)"/>
      </svg>
      <span>253-555-0187</span>
    </li>
    <li class="contact__item">
      <svg class="contact__icon" viewBox="0 0 20 20" aria-hidden="true">
        <rect x="3.5" y="5.5" width="13" height="9" fill="none" stroke="var(--ink)" stroke-width="1.6"/>
        <path d="M3.5 5.5 L10 11 L16.5 5.5" fill="none" stroke="var(--ink)" stroke-width="1.6"/>
      </svg>
      <span>ColinMarlowe@mailbox.example</span>
    </li>
    <li class="contact__item">
      <svg class="contact__icon" viewBox="0 0 20 20" aria-hidden="true">
        <circle cx="10" cy="10" r="6" fill="none" stroke="var(--ink)" stroke-width="1.5"/>
        <ellipse cx="10" cy="10" rx="2.6" ry="6" fill="none" stroke="var(--ink)" stroke-width="1.2"/>
        <line x1="4" y1="10" x2="16" y2="10" stroke="var(--ink)" stroke-width="1.2"/>
      </svg>
      <span>PorchAndRafterCheck.example</span>
    </li>
  </ul>

  <svg class="cert-badge" viewBox="0 0 112 112" role="img" aria-label="Certification badge">
    <rect x="0" y="0" width="112" height="112" fill="var(--night)"/>
    <rect x="8" y="8" width="96" height="96" fill="var(--card-white)"/>
    <circle cx="56" cy="56" r="32" fill="none" stroke="var(--badge-red)" stroke-width="6"/>
  </svg>

  <p class="license">WA Lic # 4806</p>
</section>

<section class="card card--back" aria-label="Business card back">
  <div class="back-center">
    <div class="brand">
      <span class="brand__dot"></span>
      <span>Porch and Rafter Check LLC</span>
    </div>
  </div>
</section>

</body>
</html>
```